IT Business Card Design

My company is a newly started small IT repair business. I operate outside of usual hours except for Saturday.
I am a very experienced and professional Technician.
I would like the business card to express that I am running a professional business and not some home IT business. This should be expressed through the design of the business card.
On the back of the card I would like the name of the company to be displayed.
Updates
Sorry guys, I have updated the requirement to be double sided. Fantastic submissions so far! Keep up the good work.
Hey designers!
Hey Designers!
Thank you all for your hard work!
Target Market(s)
Home to small business users.
Industry/Entity Type
Business
Contact Information for Business Card
Harbourline Computers
Marcus Pembrey (Director)
marcus.pembrey@quenmail.com.au
Operating Hours
5pm-12am Mon - Fri
9am - 5pm Sat
Mobile
0437915263
Requirements
Must have
- The base colour must be matte black. There must be some dark purple. (To go with the "Harbourline" theme)

```html
<!DOCTYPE html>
<html lang="en">
<head>
<meta charset="utf-8">
<title>Harbourline Computers – Business Card</title>
<link rel="stylesheet" href="https://fonts.googleapis.com/css2?family=Arimo:wght@400;700&display=swap">
<style>
  :root {
    --backdrop: #1c1c1c;
    --matte-black: #2b2b2b;
    --card-white: #ffffff;
    --card-shade: #d9d9d9;
    --purple: #6a35a8;
    --purple-deep: #4b2380;
    --name-grey: #b5b5b5;
    --role-grey: #4a4a4a;
    --contact-text: #f2f2f2;
  }
  * { box-sizing: border-box; margin: 0; padding: 0; }
  html, body {
    width: 1200px; height: 900px; overflow: hidden;
    background: var(--backdrop);
    font-family: "Arimo", Arial, sans-serif;
  }
  .canvas { position: relative; width: 1200px; height: 900px; }
  .card {
    position: absolute; left: 280px; width: 640px; height: 366px;
    overflow: hidden; box-shadow: 0 10px 30px rgba(0,0,0,.5);
  }
  /* back side */
  .card-back {
    top: 68px;
    background: radial-gradient(ellipse at 50% 50%, var(--card-white) 35%, var(--card-shade) 100%);
  }
  .brand-band {
    position: absolute; left: 0; right: 0; top: 150px;
    display: flex; align-items: center; gap: 22px;
  }
  .brand-rule { height: 5px; background: var(--purple); flex: 1; }
  .brand-rule.lower { position: absolute; left: 0; right: 0; top: 52px; height: 4px; background: var(--purple-deep); }
  .brand-name {
    font-weight: 700; font-size: 34px; letter-spacing: 2px;
    text-transform: uppercase; color: var(--purple); white-space: nowrap;
  }
  /* front side */
  .card-front { top: 466px; background: var(--matte-black); }
  .accent-rules { position: absolute; left: 44px; top: 0; width: 24px; height: 100%; }
  .accent-rules span { position: absolute; top: 0; bottom: 0; width: 4px; background: var(--purple); }
  .accent-rules span:first-child { left: 0; }
  .accent-rules span:last-child { left: 18px; }
  .identity { position: absolute; left: 112px; top: 96px; }
  .person-name { font-weight: 700; font-size: 30px; color: var(--name-grey); }
  .person-role { font-size: 24px; letter-spacing: 7px; color: var(--role-grey); margin-top: 2px; }
  .contact-list { position: absolute; left: 112px; top: 212px; list-style: none; }
  .contact-list li {
    display: flex; align-items: center; gap: 16px;
    color: var(--contact-text); font-size: 19px; height: 34px;
  }
  .contact-list li.phone { font-size: 23px; letter-spacing: 1px; }
  .contact-icon { width: 26px; height: 22px; flex: none; }
</style>
</head>
<body>
<main class="canvas">
  <section class="card card-back" aria-label="Card back">
    <div class="brand-band">
      <div class="brand-rule"></div>
      <span class="brand-name">Harbourline Computers</span>
      <div class="brand-rule"></div>
      <div class="brand-rule lower"></div>
    </div>
  </section>

  <section class="card card-front" aria-label="Card front">
    <div class="accent-rules"><span></span><span></span></div>
    <div class="identity">
      <p class="person-name">Marcus Pembrey</p>
      <p class="person-role">Director</p>
    </div>
    <ul class="contact-list">
      <li>
        <svg class="contact-icon" viewBox="0 0 26 22" aria-hidden="true">
          <rect x="1" y="3" width="24" height="16" fill="none" stroke="#6a35a8" stroke-width="2"/>
          <polyline points="1,3 13,13 25,3" fill="none" stroke="#6a35a8" stroke-width="2"/>
        </svg>
        marcus.pembrey@quenmail.com.au
      </li>
      <li>
        <svg class="contact-icon" viewBox="0 0 26 22" aria-hidden="true">
          <circle cx="13" cy="11" r="9" fill="none" stroke="#6a35a8" stroke-width="2"/>
          <polyline points="13,5 13,11 17,14" fill="none" stroke="#6a35a8" stroke-width="2"/>
        </svg>
        5pm-12am Mon - Fri 9am - 5pm Sat
      </li>
      <li class="phone">
        <svg class="contact-icon" viewBox="0 0 26 22" aria-hidden="true">
          <rect x="3" y="1" width="20" height="20" rx="2" fill="#6a35a8"/>
          <path d="M9 5c-1 2 0 7 4 10 2 2 4 2 5 1l-2-3-2 1c-2-1-3-3-3-5l1-1z" fill="#2b2b2b"/>
        </svg>
        043-791-5263
      </li>
    </ul>
  </section>
</main>
</body>
</html>
```